Bright Fern Accounting Postcard

I need a postcard that highlights my services and contact info. Please use the website for graphics/info... www.BrightFernAccounting.com

Target Market(s)

Business owners

Industry/Entity Type

Bookkeeper

Colors

Designer to choose colors to be used in the design.

Requirements
Must have
• Services listed, Certified Ledgerly Online Pro Advisor (can add Ledgerly logo), Contact info

```html
<!DOCTYPE html>
<html lang="en">
<head>
<meta charset="utf-8">
<title>Bright Fern Accounting Postcard</title>
<link rel="stylesheet" href="https://fonts.googleapis.com/css2?family=Bitter:wght@700&family=Lato:wght@400;700&family=Tinos&display=swap">
<style>
  :root {
    --navy: #1b3461;
    --blue: #4f87c9;
    --sky: #6fa2dd;
    --white: #ffffff;
    --backdrop: #e9eaec;
    --fern: #3f9b3a;
    --ink: #1b3461;
  }
  * { box-sizing: border-box; margin: 0; padding: 0; }
  html, body { width: 1013px; height: 1200px; overflow: hidden; background: var(--backdrop); }
  .sheet {
    position: absolute; left: 56px; top: 23px; width: 800px;
    transform: scale(1.125); transform-origin: 0 0;
    display: flex; flex-direction: column; gap: 25px;
    font-family: "Lato", Arial, sans-serif;
  }
  .card {
    position: relative; width: 800px; height: 500px;
    background: var(--white); overflow: hidden;
    box-shadow: 0 3px 10px rgba(0,0,0,.18);
  }
  .card-shapes { position: absolute; inset: 0; }
  .layer { position: absolute; }

  .brand {
    left: 20px; top: 28px; display: flex; align-items: center; gap: 8px;
    font-family: "Bitter", Georgia, serif; font-weight: 700; font-size: 25px; color: var(--navy);
  }
  .brand-mark { width: 30px; height: 30px; background: var(--navy); }

  .headline {
    left: 19px; top: 112px; width: 330px;
    font-family: "Tinos", "Times New Roman", serif; font-size: 28px; line-height: 33px; color: var(--white);
  }
  .tagline {
    left: 19px; top: 190px; width: 320px;
    font-size: 15.5px; line-height: 20px; color: var(--white);
  }
  .tab-label {
    font-family: "Tinos", "Times New Roman", serif; font-size: 15px; color: var(--navy);
  }
  .services-label { left: 19px; top: 287px; }

  .price-badge {
    left: 685px; top: 232px; width: 96px; height: 96px;
    display: flex; align-items: center; justify-content: center; text-align: center;
    font-size: 9.5px; line-height: 13px; color: var(--white);
  }

  .service { top: 325px; width: 245px; }
  .service-head { display: flex; align-items: center; gap: 9px; margin-bottom: 9px; }
  .service-icon {
    width: 32px; height: 32px; border-radius: 50%; background: var(--white);
    display: flex; align-items: center; justify-content: center;
  }
  .service-title { font-size: 13px; color: var(--sky); letter-spacing: .2px; }
  .service p {
    font-size: 9.5px; line-height: 12.6px; color: var(--white); text-align: justify;
  }
  .service-bookkeeping { left: 18px; }
  .service-reporting { left: 278px; }
  .service-payroll { left: 549px; width: 240px; }

  .web-line {
    left: 23px; top: 474px; font-size: 13px; font-weight: 700; color: var(--navy);
  }
  .contact-line {
    left: 494px; top: 464px; display: flex; align-items: center; gap: 12px;
    font-size: 18.5px; color: var(--navy);
  }
  .contact-line .phone { margin-left: 8px; }

  .vision-label { left: 19px; top: 262px; font-family: "Tinos", "Times New Roman", serif; font-size: 15px; color: var(--white); }
  .vision-text { left: 17px; top: 307px; width: 355px; }
  .vision-text p {
    font-size: 9.5px; line-height: 12.5px; color: var(--white); text-align: justify; margin-bottom: 12px;
  }
  .quote-call {
    left: 0; top: 455px; width: 370px; text-align: center;
    font-size: 13.5px; line-height: 19px; color: var(--navy);
  }
  .quote-call .site { color: var(--blue); font-weight: 700; }
</style>
</head>
<body>
<main class="sheet">

  <!-- Front -->
  <section class="card card-front">
    <svg class="card-shapes" viewBox="0 0 800 500" width="800" height="500">
      <defs>
        <linearGradient id="officeTone" x1="0" y1="0" x2="1" y2="1">
          <stop offset="0" stop-color="#c9d8ea"/>
          <stop offset=".55" stop-color="#8fb0d6"/>
          <stop offset="1" stop-color="#3d5f8f"/>
        </linearGradient>
      </defs>
      <rect x="340" y="0" width="460" height="280" fill="url(#officeTone)" role="img" aria-label="Photo of a business meeting with a laptop showing accounting software"/>
      <rect x="0" y="95" width="362" height="185" fill="var(--blue)"/>
      <path d="M382 0 H394 L377 95 H365 Z" fill="var(--navy)"/>
      <path d="M372 0 H384 L367 95 H355 Z" fill="var(--blue)"/>
      <path d="M0 0 H372 L355 95 H0 Z" fill="var(--white)"/>
      <rect x="0" y="280" width="800" height="182" fill="var(--navy)"/>
      <path d="M0 280 H163 L153 308 H0 Z" fill="var(--white)"/>
      <circle cx="347" cy="270" r="22" fill="var(--fern)"/>
      <circle cx="733" cy="280" r="48" fill="var(--blue)"/>
      <rect x="0" y="462" width="800" height="38" fill="var(--white)"/>
      <path d="M416 500 L426 446 H438 L428 500 Z" fill="var(--blue)"/>
      <path d="M430 500 L440 443 H452 L442 500 Z" fill="var(--navy)"/>
      <path d="M446 500 L456 441 H800 V500 Z" fill="var(--white)"/>
    </svg>

    <div class="layer brand"><span class="brand-mark"></span>Bright Fern Accounting</div>
    <h1 class="layer headline">BOUTIQUE<br>ACCOUNTING FIRM</h1>
    <p class="layer tagline">Specializing in Small Business Bookkeeping &amp; Payroll Processing with Ledgerly Online by Corvane.</p>
    <div class="layer tab-label services-label">SERVICES</div>
    <div class="layer price-badge">Full Service<br>Bookkeeping<br>Starting at $395/mo.</div>

    <article class="layer service service-bookkeeping">
      <div class="service-head">
        <span class="service-icon">
          <svg width="20" height="20" viewBox="0 0 20 20"><ellipse cx="10" cy="5" rx="7" ry="3" fill="var(--navy)"/><path d="M3 8 Q10 12 17 8 V10 Q10 14 3 10 Z M3 12 Q10 16 17 12 V14 Q10 18 3 14 Z" fill="var(--navy)"/></svg>
        </span>
        <h2 class="service-title">BOOKKEEPING</h2>
      </div>
      <p>Let us take over the day to day bookkeeping so you can get back to running your business. We offer Ledgerly Online setup and ongoing bookkeeping, including daily journal entries, accounts payables &amp; receivables, bill pay, sales tax reporting &amp; payments, account reconciliation, and more.</p>
    </article>

    <article class="layer service service-reporting">
      <div class="service-head">
        <span class="service-icon">
          <svg width="20" height="20" viewBox="0 0 20 20"><rect x="3" y="2" width="14" height="16" fill="none" stroke="var(--navy)" stroke-width="1.6"/><rect x="6" y="10" width="2" height="5" fill="var(--navy)"/><rect x="9" y="7" width="2" height="8" fill="var(--navy)"/><rect x="12" y="5" width="2" height="10" fill="var(--navy)"/></svg>
        </span>
        <h2 class="service-title">FINANCIAL REPORTING</h2>
      </div>
      <p>We'll provide easy to understand financial reports that allow you and your team to manage cash flow, create budgets and make forecasting decisions. Want real time data? Let us provide solutions with the latest in mobile apps and dashboards.</p>
    </article>

    <article class="layer service service-payroll">
      <div class="service-head">
        <span class="service-icon">
          <svg width="20" height="20" viewBox="0 0 20 20"><circle cx="6" cy="6" r="2.5" fill="var(--navy)"/><circle cx="14" cy="6" r="2.5" fill="var(--navy)"/><path d="M2 15 Q6 8 10 15 Z M10 15 Q14 8 18 15 Z" fill="var(--navy)"/></svg>
        </span>
        <h2 class="service-title">PAYROLL PROCESSING</h2>
      </div>
      <p>Whether you have 5 employees or 100+, payroll can be an overwhelming and time consuming task. We offer full service payroll processing, including employee on boarding and reporting.</p>
    </article>

    <div class="layer web-line">brightfernaccounting.com | info@brightfernaccounting.com</div>
    <div class="layer contact-line">
      <span>CONTACT US</span>
      <svg width="16" height="16" viewBox="0 0 16 16"><circle cx="8" cy="8" r="7" fill="none" stroke="var(--navy)" stroke-width="1.5"/><path d="M5.5 4.5 L7 4.5 L7.5 6.5 L6.6 7.3 Q7.5 9 8.9 9.6 L9.7 8.7 L11.5 9.2 L11.5 10.6 Q8 11.5 5.5 7.5 Z" fill="var(--navy)"/></svg>
      <span class="phone">1.877.555.0142</span>
    </div>
  </section>

  <!-- Back -->
  <section class="card card-back">
    <svg class="card-shapes" viewBox="0 0 800 500" width="800" height="500">
      <defs>
        <linearGradient id="deskTone" x1="0" y1="0" x2="1" y2="1">
          <stop offset="0" stop-color="#6f8fb8"/>
          <stop offset=".5" stop-color="#c4d3e6"/>
          <stop offset="1" stop-color="#5a7fae"/>
        </linearGradient>
      </defs>
      <rect x="0" y="95" width="392" height="150" fill="url(#deskTone)" role="img" aria-label="Photo of hands reviewing financial charts on a tablet"/>
      <path d="M382 0 H394 L377 95 H365 Z" fill="var(--navy)"/>
      <path d="M372 0 H384 L367 95 H355 Z" fill="var(--blue)"/>
      <path d="M0 0 H372 L355 95 H0 Z" fill="var(--white)"/>
      <rect x="0" y="245" width="392" height="45" fill="var(--blue)"/>
      <rect x="0" y="290" width="392" height="152" fill="var(--navy)"/>
      <path d="M0 442 H392 V500 H0 Z" fill="var(--white)"/>
      <path d="M374 442 H386 L397 500 H385 Z" fill="var(--blue)"/>
      <path d="M386 442 H392 L403 500 H397 Z" fill="var(--navy)"/>
      <rect x="673.5" y="27.5" width="102" height="73" fill="none" stroke="#d6d9de"/>
      <g stroke="#d6d9de" stroke-width="1">
        <line x1="452" y1="180" x2="775" y2="180"/>
        <line x1="452" y1="225" x2="775" y2="225"/>
        <line x1="452" y1="270" x2="775" y2="270"/>
        <line x1="452" y1="316" x2="775" y2="316"/>
      </g>
    </svg>

    <div class="layer brand"><span class="brand-mark"></span>Bright Fern Accounting</div>
    <div class="layer vision-label">OUR VISION</div>
    <div class="layer vision-text">
      <p>At Bright Fern Accounting we have one mission in mind... to improve the quality, accuracy and efficiency of your business's back-end bookkeeping and payroll processing, so that you can focus on the nuts and bolts of your day to day operations.</p>
      <p>Founded by a former CFO in the San Francisco Bay Area, we bring a team of accounting professionals with over 20 years of expertise from one of the most competitive markets in the world.</p>
    </div>
    <div class="layer quote-call">
      Contact us today for your no obligation quote!<br>
      <span class="site">www.BrightFernAccounting.com</span>
    </div>
  </section>

</main>
</body>
</html>
```